Stationery for Brightfield Pest Control
Business Cards, Letterhead, Envelopes, Folder, MemoPad, and E-Mail Signature
Stationery for Brightfield Pest Control  - Corporate Services
Creative Brief
Professional
Dana Pellborough
Owner
417 Calloway Street Halden Ridge, OR, 58216
kmolegrove@mailvessel.com
www.gobrightfieldpest.com
OR Lic.#52734
I would like the be able to do editing to business cards and letterhead so that multiple peaple can use.
Concepts
Business Cards and Stationery for Background Check Company
Business Cards and Stationery for new compliance company.

```html
<!DOCTYPE html>
<html lang="en">
<head>
<meta charset="utf-8">
<title>Brightfield Pest Control – Business Card</title>
<link rel="stylesheet" href="https://fonts.googleapis.com/css2?family=Montserrat:wght@400;600;800&family=Open+Sans:wght@400;600&display=swap">
<style>
  :root {
    --green: #1f7a3c;
    --green-dark: #145c2b;
    --green-light: #2f9550;
    --white: #ffffff;
    --paper: #f4f4f2;
    --rule: #c9cbc8;
    --stage: #e8e6e1;
    --ink-soft: #5c625e;
    --bug-tone: #b9c6bd;
  }
  * { margin: 0; padding: 0; box-sizing: border-box; }
  html, body { width: 1200px; height: 794px; overflow: hidden; }
  body {
    background: var(--stage);
    font-family: "Open Sans", Arial, sans-serif;
    position: relative;
  }
  .card {
    position: absolute;
    width: 520px;
    height: 300px;
    border-radius: 18px;
    overflow: hidden;
    box-shadow: 0 6px 18px rgba(0,0,0,0.18);
  }
  .card-back {
    left: 50px; top: 247px;
    background: linear-gradient(150deg, var(--green-light), var(--green) 55%, var(--green-dark));
  }
  .card-back .emblem-area {
    position: absolute;
    left: 214px; top: 70px;
    width: 92px; height: 110px;
    border-radius: 46px;
    background: radial-gradient(circle, var(--bug-tone), rgba(185,198,189,0.55));
  }
  .card-back .web {
    position: absolute;
    left: 0; right: 0; top: 212px;
    text-align: center;
    color: var(--bug-tone);
    font-size: 13px;
    letter-spacing: 3px;
  }
  .card-front { left: 630px; top: 247px; background: var(--green); }
  .card-front svg.shape { position: absolute; inset: 0; }
  .brand {
    position: absolute;
    left: 300px; top: 92px;
    width: 210px;
    display: flex; align-items: center; gap: 10px;
  }
  .brand-dot {
    flex: 0 0 46px; height: 46px; border-radius: 50%;
    background: var(--green);
  }
  .brand-name {
    font-family: "Montserrat", Arial, sans-serif;
    font-weight: 800;
    font-size: 19px;
    line-height: 1.1;
    color: var(--green);
  }
  .address {
    position: absolute;
    right: 22px; bottom: 20px;
    text-align: right;
    font-size: 11px;
    line-height: 1.5;
    color: var(--ink-soft);
  }
  .person { position: absolute; left: 26px; top: 28px; color: var(--white); }
  .person-name { font-family: "Montserrat", Arial, sans-serif; font-weight: 600; font-size: 18px; }
  .person-role { font-size: 11px; opacity: 0.85; margin-top: 2px; }
  .contacts {
    position: absolute; left: 26px; top: 118px;
    list-style: none; color: var(--white);
    font-size: 11px; line-height: 1.9;
  }
  .contacts li { display: flex; align-items: center; gap: 8px; }
  .contacts svg { width: 11px; height: 11px; flex: 0 0 11px; }
</style>
</head>
<body>

<section class="card card-back">
  <div class="emblem-area" role="img" aria-label="Beetle emblem of the company"></div>
  <p class="web">www.gobrightfieldpest.com</p>
</section>

<section class="card card-front">
  <svg class="shape" width="520" height="300" viewBox="0 0 520 300" aria-hidden="true">
    <path d="M262 0 H520 V300 H262 V190 C262 170 282 165 282 150 C282 135 262 130 262 110 Z"
          fill="var(--paper)" stroke="var(--rule)" stroke-width="6"/>
    <path d="M262 0 H520 V300 H262 V190 C262 170 282 165 282 150 C282 135 262 130 262 110 Z"
          fill="var(--white)"/>
  </svg>

  <div class="brand">
    <span class="brand-dot"></span>
    <span class="brand-name">Brightfield Pest Control</span>
  </div>

  <p class="address">417 Calloway Street<br>Halden Ridge, OR 58216</p>

  <div class="person">
    <p class="person-name">Dana Pellborough</p>
    <p class="person-role">Owner</p>
  </div>

  <ul class="contacts">
    <li><svg viewBox="0 0 12 12"><path d="M3 1 L5 3.5 L4 5 C5 7 6 8 7.5 8.5 L9 7.5 L11 9.5 L9.5 11 C5 10.5 1.5 7 1 2.5 Z" fill="#fff"/></svg>555.014.2290</li>
    <li><svg viewBox="0 0 12 12"><rect x="1.5" y="4" width="9" height="6" rx="1" fill="#fff"/><rect x="3.5" y="1" width="5" height="3" fill="#fff"/></svg>555.014.7731</li>
    <li><svg viewBox="0 0 12 12"><rect x="3.5" y="1" width="5" height="10" rx="1" fill="#fff"/></svg>555.014.5508</li>
    <li><svg viewBox="0 0 12 12"><rect x="1" y="3" width="10" height="7" fill="none" stroke="#fff"/><path d="M1 3 L6 7 L11 3" fill="none" stroke="#fff"/></svg>kmolegrove@mailvessel.com</li>
    <li><svg viewBox="0 0 12 12"><circle cx="6" cy="6" r="4.5" fill="none" stroke="#fff"/><path d="M1.5 6 H10.5 M6 1.5 V10.5" stroke="#fff"/></svg>www.gobrightfieldpest.com</li>
    <li><svg viewBox="0 0 12 12"><path d="M2 6.5 L5 9 L10 3" fill="none" stroke="#fff" stroke-width="1.6"/></svg>OR Lic.#52734</li>
  </ul>
</section>

</body>
</html>
```